依頼詳細
デザインをお願いする当サイトのトップページの役割は、
・当該部門の抽象的イメージの表現
・各種コンテンツ(製品情報、ブログ記事)のポータル的機能
の2つを主軸に据えようと考えています。

デザインの条件として、
・サイトロゴはこちから指定したものを使用する。
・レスポンシブデザインを適用する。
とさせて頂きます。ついては、

開発したアプリ、サービス等の周知、蓄積した技術情報等の発信を行うためにWebサイトとして見栄えがする、
・ページ全体、および個々の要素の配色
・ボーダー、シャドウのデザイン
・各要素の質感
のデザインをご提案頂きたいです。

現在、こちらで添付のようなページレイアウトを検討していますが、あくまで案ですので、レイアウトも含めたデザインをご提案いただいても構いません。
ページ数
1ページ
希望イメージ
シンプル 複雑
単色 カラフル
暗い 明るい
日常 高級
遊び心 厳粛
未来的 伝統的
女性的 男性的
希望する色
ロゴのカラーバリエーションのいずれかにマッチする配色でお願いします。
納品ファイル
• 高解像度JPG (.jpg)
• イラストレーター形式 (.ai)
• フォトショップ形式 (.psd)
• PNG形式 (.png)
補足説明
ロゴには、カラーバリエーションがありますので、サイト全体の配色に合うものを
適宜選択していただければと思います。
〆切を延長させて頂きます。
■ 選んだ理由

シンプルでわかりやすいデザインがサイトにマッチすると思いました。

■ 提案者全員のお礼・コメント

たくさんのご提案をありがとうございます。
今後ともよろしくお願いします。

```html
<!DOCTYPE html>
<html lang="ja">
<head>
<meta charset="utf-8">
<title>NQ Works</title>
<link href="https://fonts.googleapis.com/css2?family=Noto+Sans+JP:wght@400;500;700&family=Roboto:wght@400;500;700&display=swap" rel="stylesheet">
<style>
:root{
  --yellow:#f6c418;
  --yellow-deep:#e8b40c;
  --dark:#343434;
  --dark-2:#3f3f3f;
  --footer:#4a4a4a;
  --grey-bg:#e9e9e9;
  --text:#2d2d2d;
  --muted:#9a9a9a;
  --white:#ffffff;
}
*{box-sizing:border-box;margin:0;padding:0}
html,body{width:738px;height:1200px;overflow:hidden;background:var(--white)}
body{font-family:"Noto Sans JP","Roboto",sans-serif;color:var(--text)}
.page{position:relative;width:738px;height:1200px;overflow:hidden;background:var(--grey-bg)}

.site-header{position:absolute;left:0;top:0;width:738px;height:69px;background:var(--white);border-bottom:2px solid var(--yellow)}
.brand{position:absolute;display:flex;align-items:center;gap:6px;font-family:"Roboto",sans-serif;font-weight:700;color:var(--yellow)}
.brand-dot{width:14px;height:14px;border-radius:50%;background:var(--yellow)}
.site-header .brand{left:14px;top:22px;font-size:20px}
.main-nav{position:absolute;right:40px;top:0;height:67px;display:flex;font-family:"Roboto",sans-serif;font-size:9px;letter-spacing:.5px}
.main-nav a{display:block;padding:44px 15px 0;height:67px;color:var(--text);text-decoration:none}
.main-nav a.is-current{background:var(--yellow);color:var(--white)}

.hero{position:absolute;left:0;top:69px;width:738px;height:288px;background:linear-gradient(100deg,#d9dcdf 0%,#eef0f1 40%,#b9bec3 75%,#8e959b 100%)}
.hero-panel{position:absolute;left:258px;top:54px;width:222px;height:124px;background:rgba(255,255,255,.72);padding:20px 22px}
.hero-panel .brand{position:static;font-size:26px;color:var(--dark)}
.hero-panel .brand-dot{width:18px;height:18px;background:var(--yellow)}
.hero-panel p{margin-top:10px;font-size:8px;line-height:1.6;color:#555}

.products-band{position:absolute;left:0;top:357px;width:738px;height:81px;background:var(--dark);color:var(--white);text-align:center;font-family:"Roboto",sans-serif;font-size:19px;letter-spacing:1px;line-height:81px}
.products{position:absolute;left:49px;top:438px;width:640px;height:108px;display:flex;gap:10px}
.product-card{flex:1;background:var(--yellow);display:flex;align-items:center;padding:0 14px}
.product-icon{width:70px;text-align:center;color:var(--white);font-family:"Roboto",sans-serif;font-size:13px;border-right:1px solid rgba(255,255,255,.7);padding-right:10px}
.product-icon svg{display:block;margin:0 auto 6px}
.product-card p{padding-left:14px;font-size:8.5px;line-height:1.7;color:var(--text)}

.blog{position:absolute;left:49px;top:610px;width:640px;height:337px;display:flex}
.blog-lead{position:relative;width:163px;height:337px;background:linear-gradient(160deg,#f4f4f4 0%,#cfd3c6 55%,#9aa48a 100%)}
.blog-lead h2{position:absolute;left:10px;top:22px;font-family:"Roboto",sans-serif;font-weight:500;font-size:17px;line-height:1.15;color:var(--dark)}
.more-button{position:absolute;left:13px;top:288px;width:135px;height:32px;background:var(--yellow);color:var(--white);font-size:12px;line-height:32px;padding-left:14px}
.more-button svg{position:absolute;right:10px;top:11px}
.blog-grid{flex:1;display:grid;grid-template-columns:repeat(3,1fr);grid-template-rows:repeat(2,1fr)}
.post{display:flex;flex-direction:column;border-left:1px solid var(--grey-bg)}
.post:nth-child(n+4){border-top:1px solid var(--grey-bg)}
.post-photo{height:95px}
.post-body{flex:1;background:var(--dark-2);padding:10px 10px;color:var(--white)}
.post-body h3{font-size:11px;font-weight:400;line-height:1.45}
.post-body time{display:block;margin-top:4px;font-size:7px;color:var(--muted)}
.ph-a{background:linear-gradient(135deg,#e5e5e5,#9b9b9b)}
.ph-b{background:linear-gradient(135deg,#dfeef6,#a9c9da)}
.ph-c{background:linear-gradient(135deg,#eeeeee,#b7c1cc)}
.ph-d{background:linear-gradient(135deg,#3b3326,#c9a24a)}
.ph-e{background:linear-gradient(135deg,#f1f1f1,#9ea7ae)}
.ph-f{background:linear-gradient(135deg,#d8d8d8,#6f7478)}

.to-top{position:absolute;left:660px;top:965px;width:29px;height:29px;background:var(--dark);display:flex;align-items:center;justify-content:center}

.site-footer{position:absolute;left:0;top:1004px;width:738px;height:161px;background:var(--footer)}
.site-footer .brand{left:49px;top:26px;font-size:20px}
.footer-note{position:absolute;left:49px;top:62px;width:150px;font-size:8px;line-height:1.6;color:#d6d6d6}
.contact-button{position:absolute;left:370px;top:71px;width:319px;height:37px;background:var(--yellow);color:var(--text);font-size:14px;line-height:37px;padding-left:120px}
.contact-button svg{position:absolute;right:14px;top:12px}
.footer-bar{position:absolute;left:0;top:1165px;width:738px;height:35px;background:var(--white);font-size:8px;color:#666;line-height:35px}
.footer-bar small{position:absolute;left:49px;font-size:8px}
.footer-links{position:absolute;right:40px;display:flex;gap:22px}
</style>
</head>
<body>
<div class="page">

  <header class="site-header">
    <div class="brand"><span class="brand-dot"></span>NQ Works</div>
    <nav class="main-nav">
      <a class="is-current" href="#">HOME</a>
      <a href="#">PRODUCTS</a>
      <a href="#">BLOG</a>
      <a href="#">CONTACTS</a>
    </nav>
  </header>

  <section class="hero" role="img" aria-label="タブレットを操作する手のイメージ写真">
    <div class="hero-panel">
      <div class="brand"><span class="brand-dot"></span>NQ Works</div>
      <p>アプリとサービスの開発で<br>新しい技術を発信しています<br>私たちの取り組みをご紹介します</p>
    </div>
  </section>

  <div class="products-band">PRODUCTS</div>

  <section class="products">
    <article class="product-card">
      <div class="product-icon">
        <svg width="22" height="34" viewBox="0 0 22 34" fill="none" stroke="#fff" stroke-width="1.6"><rect x="1" y="1" width="20" height="32" rx="3"/><line x1="8" y1="28" x2="14" y2="28"/></svg>
        APP
      </div>
      <p>スマートフォン向けアプリの情報を掲載しています。開発中の新作や更新情報もこちらでご覧ください。</p>
    </article>
    <article class="product-card">
      <div class="product-icon">
        <svg width="34" height="34" viewBox="0 0 34 34" fill="none" stroke="#fff" stroke-width="1.6"><circle cx="17" cy="17" r="15"/><ellipse cx="17" cy="17" rx="6.5" ry="15"/><line x1="2" y1="17" x2="32" y2="17"/></svg>
        WEB
      </div>
      <p>ウェブサービスの情報を掲載しています。提供中のサービスと技術資料をこちらでご確認ください。</p>
    </article>
  </section>

  <section class="blog">
    <div class="blog-lead" role="img" aria-label="Innovationと書かれたキーボードの写真">
      <h2>RECENT FROM<br>BLOG</h2>
      <a class="more-button">もっと見る
        <svg width="7" height="10" viewBox="0 0 7 10"><path d="M1 1l4 4-4 4" stroke="#fff" stroke-width="1.6" fill="none"/></svg>
      </a>
    </div>
    <div class="blog-grid">
      <article class="post"><div class="post-photo ph-a" role="img" aria-label="回路基板の写真"></div><div class="post-body"><h3>ブログタイトルブログタイトル</h3><time>2015/08/00 00:00:00</time></div></article>
      <article class="post"><div class="post-photo ph-b" role="img" aria-label="ケーブルの写真"></div><div class="post-body"><h3>ブログタイトルブログタイトル</h3><time>2015/08/00 00:00:00</time></div></article>
      <article class="post"><div class="post-photo ph-c" role="img" aria-label="グラフ資料の写真"></div><div class="post-body"><h3>ブログタイトルブログタイトル</h3><time>2015/08/00 00:00:00</time></div></article>
      <article class="post"><div class="post-photo ph-d" role="img" aria-label="金色の部品の写真"></div><div class="post-body"><h3>ブログタイトルブログタイトル</h3><time>2015/08/00 00:00:00</time></div></article>
      <article class="post"><div class="post-photo ph-e" role="img" aria-label="ノートパソコンの写真"></div><div class="post-body"><h3>ブログタイトルブログタイトル</h3><time>2015/08/00 00:00:00</time></div></article>
      <article class="post"><div class="post-photo ph-f" role="img" aria-label="キーボード操作の写真"></div><div class="post-body"><h3>ブログタイトルブログタイトル</h3><time>2015/08/00 00:00:00</time></div></article>
    </div>
  </section>

  <a class="to-top" aria-label="ページトップへ">
    <svg width="12" height="8" viewBox="0 0 12 8"><path d="M1 7l5-5 5 5" stroke="#fff" stroke-width="1.8" fill="none"/></svg>
  </a>

  <footer class="site-footer">
    <div class="brand"><span class="brand-dot"></span>NQ Works</div>
    <p class="footer-note">技術情報とアプリの最新情報を<br>お届けする開発部門のサイト<br>です。お気軽にどうぞ。</p>
    <a class="contact-button">お問い合わせ
      <svg width="14" height="12" viewBox="0 0 14 12"><path d="M1 6h11M8 2l4 4-4 4" stroke="#2d2d2d" stroke-width="1.6" fill="none"/></svg>
    </a>
  </footer>
  <div class="footer-bar">
    <small>Copyright 2015 NQ Works All Rights Reserved</small>
    <nav class="footer-links"><span>ホーム</span><span>製品情報</span><span>ブログ</span><span>お問い合わせ</span></nav>
  </div>

</div>
</body>
</html>
```